Bramwell Builders Web Site / Business Cards

Construction Company that specializes in Water and Fire Damage, Residential ReModels, Landscaping and Building ADU (Accessory Dwelling Unit)

Growing and changing families often need additional space, and a remodeling project can often provide that. Adding a new area, or repurposing an existing one can satisfy this requirement.

Other times, homeowners want to update the look in their kitchen or bathroom with more than just a change of cabinetry or vanity doors and drawers. Whatever your needs are, Bramwell Builders has skilled workers who are bonded and insured, and ready to make your dreams and visions a reality.

Target Market(s)

Home Owners

Industry/Entity Type

Construction Company

Contact Information for Business Card

Center Logo with our information on the corners

Back side to be Logo Only
Contact Info
SBRQ License # 5820914
info@bramwellbuildersca.example
www.bramwellbuildersca.example

Coding

Coded - Design and coding required

Number of Pages Required

5+ page

Font styles to use
Serif
Sans Serif

Requirements
Must have
• Using our Logo Colors
Home
About Us
Services
Projects / Portfolio
Contact Us
Nice to have
• Colors matching our Logo
Should not have
• Black because it doesnt match our logo

```html
<!DOCTYPE html>
<html lang="en">
<head>
<meta charset="utf-8">
<title>Bramwell Builders</title>
<link href="https://fonts.googleapis.com/css2?family=Merriweather:wght@400;700&family=Open+Sans:ital,wght@0,400;0,600;0,700;1,400&display=swap" rel="stylesheet">
<style>
:root{
  --orange:#f26f21;
  --orange-soft:#f58a45;
  --ink:#2f2f33;
  --text:#6a6a70;
  --line:#c9c9cd;
  --grey-band:#e7e7e8;
  --white:#ffffff;
}
*{box-sizing:border-box;margin:0;padding:0}
html,body{width:1200px;height:3729px;overflow:hidden;background:var(--white)}
body{position:relative;font-family:"Open Sans",sans-serif;color:var(--text)}
.abs{position:absolute}
.serif{font-family:"Merriweather",serif}

/* header */
.social-round{width:36px;height:36px;border:2px solid var(--orange);border-radius:50%;position:absolute}
.top-email{left:797px;top:40px;font-size:18px;color:var(--ink);display:flex;align-items:center;gap:10px}
.nav-bar{left:0;top:104px;width:1200px;height:44px;background:var(--orange)}
.nav-link{position:absolute;top:114px;font-family:"Merriweather",serif;font-size:17px;color:var(--white)}
.nav-link.active{color:var(--ink)}
.logo-badge{left:455px;top:-61px;width:290px;height:290px;border-radius:50%;background:var(--white);z-index:3}
.logo-name{left:455px;top:120px;width:290px;text-align:center;z-index:4;font-family:"Open Sans",sans-serif;font-weight:700;font-size:30px;line-height:34px;letter-spacing:3px;color:var(--ink)}

/* hero */
.hero{left:0;top:148px;width:1200px;height:634px;
  clip-path:polygon(0 0,1200px 0,1200px 511px,376px 634px,0 511px);
  background:linear-gradient(180deg,#6e6a84 0%,#c9808e 18%,#dc8f90 28%,#9a9498 48%,#7b7670 68%,#4b4742 100%)}
.hero-title{left:0;top:245px;width:1200px;text-align:center;font-family:"Merriweather",serif;font-weight:700;font-size:80px;color:var(--white)}
.hero-sub{left:250px;top:360px;width:700px;text-align:center;font-size:25px;line-height:41px;color:var(--white)}
.hero-btn{left:481px;top:466px;width:238px;height:67px;background:var(--white);border-radius:4px;display:flex;align-items:center;justify-content:center;font-weight:600;font-size:20px;color:var(--ink)}
.hero-arrow{top:389px;width:38px;height:48px;background:rgba(40,40,44,.75);display:flex;align-items:center;justify-content:center}

/* welcome */
.welcome-title{left:111px;top:808px;font-family:"Merriweather",serif;font-weight:700;font-size:44px;line-height:54px;color:var(--ink)}
.welcome-copy{left:111px;width:470px;font-size:15.5px;line-height:28px}
.btn{background:var(--orange);color:var(--white);border-radius:3px;font-weight:700;display:flex;align-items:center;justify-content:center}
.welcome-video{left:599px;top:827px;width:490px;height:305px;background:linear-gradient(135deg,#c9c3b8,#8b8478 55%,#6a655e);box-shadow:0 4px 10px rgba(0,0,0,.2)}

/* services */
.services-band{left:0;top:1223px;width:1200px;height:641px;
  clip-path:polygon(0 87px,803px 0,1200px 87px,1200px 521px,311px 641px,0 531px);
  background:linear-gradient(120deg,#f0752c,#f2894a 45%,#ee6d22)}
.section-title{left:0;width:1200px;text-align:center;font-family:"Merriweather",serif;font-weight:700;font-size:44px;color:var(--ink)}
.service-card{top:1381px;width:236px;height:357px;background:rgba(255,255,255,.18)}
.service-card.featured{background:var(--white)}
.service-photo{width:236px;height:169px}
.service-name{position:absolute;left:15px;top:190px;font-family:"Merriweather",serif;font-weight:700;font-size:19.5px;color:var(--white);white-space:nowrap}
.service-copy{position:absolute;left:15px;top:228px;width:210px;font-size:14px;line-height:23px;color:#fde6d6}
.service-more{position:absolute;left:15px;top:314px;font-size:15px;font-weight:700;color:var(--white)}
.featured .service-name{color:var(--ink)}
.featured .service-copy{color:var(--text)}
.featured .service-more{color:var(--orange)}

/* projects */
.project-tile{width:319px;height:234px}

/* testimonials */
.testimonial-band{left:0;top:2678px;width:1200px;height:444px;
  clip-path:polygon(0 46px,600px 0,1200px 36px,1200px 359px,866px 444px,0 326px);
  background:var(--grey-band)}
.quote-circle{left:111px;top:2767px;width:212px;height:212px;border-radius:50%;background:var(--white)}
.quote-mark{left:138px;top:2808px;font-family:"Merriweather",serif;font-weight:700;font-size:110px;line-height:1;color:var(--orange)}
.client-photo{left:224px;top:2767px;width:212px;height:212px;border-radius:50%;background:linear-gradient(160deg,#c6c3c0,#8e847c 55%,#5a5049)}
.quote-text{left:481px;top:2803px;width:610px;font-style:italic;font-size:17.5px;line-height:33px;color:#6b6b70}
.quote-name{left:487px;top:2920px;font-size:20px;font-weight:600;color:var(--ink)}
.dot-arrow{top:3012px;width:27px;height:27px;border-radius:50%;background:#8d8d91;display:flex;align-items:center;justify-content:center}

/* contact */
.sub-title{font-size:22px;color:var(--ink)}
.field{border:1.5px solid var(--line);border-radius:3px;font-size:15px;color:#666;padding:12px 14px}
.info-icon{left:779px;width:34px;height:34px;border:1.5px solid var(--line);border-radius:50%;display:flex;align-items:center;justify-content:center}
.info-text{left:829px;font-size:15px;line-height:24px;color:#6a6a70}
.social-small{top:3541px;width:36px;height:36px;border:1.5px solid var(--line);border-radius:50%}
.footer-rule{left:111px;top:3630px;width:970px;height:1px;background:var(--line)}
.copyright{left:0;top:3669px;width:1200px;text-align:center;font-size:15px;color:#6a6a70}
</style>
</head>
<body>

<!-- header -->
<div class="social-round" style="left:111px;top:35px" role="img" aria-label="Social profile link"></div>
<div class="social-round" style="left:156px;top:35px" role="img" aria-label="Social profile link"></div>
<div class="social-round" style="left:201px;top:35px" role="img" aria-label="Social profile link"></div>
<div class="abs top-email">
  <svg width="18" height="14" viewBox="0 0 18 14"><rect width="18" height="14" rx="2" fill="#f26f21"/><path d="M1 2l8 6 8-6" stroke="#fff" stroke-width="1.6" fill="none"/></svg>
  info@bramwellbuildersca.example
</div>

<!-- hero -->
<div class="abs hero" role="img" aria-label="Large stone house with lit windows at sunset"></div>
<div class="abs nav-bar"></div>
<span class="nav-link active" style="left:110px">Home</span>
<span class="nav-link" style="left:221px">About Us</span>
<span class="nav-link" style="left:360px">Services</span>
<span class="nav-link" style="left:790px">Projects</span>
<span class="nav-link" style="left:931px">Contact Us</span>
<svg class="abs" style="left:1074px;top:118px" width="16" height="16" viewBox="0 0 16 16"><circle cx="6.5" cy="6.5" r="5" stroke="#fff" stroke-width="2.4" fill="none"/><path d="M10 10l4.5 4.5" stroke="#fff" stroke-width="2.6"/></svg>
<div class="abs logo-badge"></div>
<div class="abs logo-name">BRAMWELL<br>BUILDERS</div>

<h1 class="abs hero-title">Bramwell Builders</h1>
<p class="abs hero-sub">We specializes in Water and Fire Damage, Residential ReModels, Landscaping and Building ADU</p>
<div class="abs hero-btn">REQUEST A QUOTE</div>
<div class="abs hero-arrow" style="left:0"><svg width="12" height="20" viewBox="0 0 12 20"><path d="M10 2L3 10l7 8" stroke="#fff" stroke-width="2.4" fill="none"/></svg></div>
<div class="abs hero-arrow" style="left:1162px"><svg width="12" height="20" viewBox="0 0 12 20"><path d="M2 2l7 8-7 8" stroke="#fff" stroke-width="2.4" fill="none"/></svg></div>

<!-- welcome -->
<h2 class="abs welcome-title">Welcome to<br>Bramwell Builders</h2>
<p class="abs welcome-copy" style="top:941px">Nemo enim ipsam voluptatem quia voluptas sit aspernatur aodit aut fugit, sed quia consequuntur mag.</p>
<p class="abs welcome-copy" style="top:1025px">Sni dolores eos qui ratione voluptatem sequi nesciunt. Neque po rro quisquam est, qui dolorem ipsum quia dolor sit amet, conser ctetur, adipisci velit, sed quia non numquam eius modi tempora incidunt ut labore et dolore magn.</p>
<div class="abs btn" style="left:111px;top:1167px;width:160px;height:58px;font-size:16px">READ MORE</div>
<div class="abs welcome-video" role="img" aria-label="Video still of two builders reviewing plans in a room under renovation"></div>
<svg class="abs" style="left:813px;top:948px" width="64" height="64" viewBox="0 0 64 64"><circle cx="32" cy="32" r="32" fill="#2b2b2e"/><path d="M25 19l21 13-21 13z" fill="#fff"/></svg>

<!-- services -->
<div class="abs services-band" role="img" aria-label="Orange band over a faint worksite photo"></div>
<h2 class="abs section-title" style="top:1305px;color:#fff">Our Services</h2>

<div class="abs service-card" style="left:111px">
  <div class="service-photo" role="img" aria-label="Power plug in a wall socket beside water damage" style="background:linear-gradient(135deg,#5c5c5e,#a5a5a7 50%,#3a3a3c)"></div>
  <div class="service-name">Water &amp; Fire Damage</div>
  <p class="service-copy">Ut enim ad minima veniamu is nostrum exercitationeull am corporis suscip.</p>
  <div class="service-more">READ MORE</div>
</div>
<div class="abs service-card featured" style="left:358px">
  <div class="service-photo" role="img" aria-label="Worker fitting a roof window in a timber attic" style="background:linear-gradient(135deg,#d9c4a0,#efe6d4 45%,#8aa0b8)"></div>
  <div class="service-name">Residential ReModels</div>
  <p class="service-copy">Ut enim ad minima veniamu is nostrum exercitationeull am corporis suscip.</p>
  <div class="service-more">READ MORE</div>
</div>
<div class="abs service-card" style="left:605px">
  <div class="service-photo" role="img" aria-label="Gardener laying rolls of turf" style="background:linear-gradient(135deg,#8c7a58,#5f8a2c 50%,#3f6d1e)"></div>
  <div class="service-name">Landscaping</div>
  <p class="service-copy">Ut enim ad minima veniamu is nostrum exercitationeull am corporis suscip.</p>
  <div class="service-more">READ MORE</div>
</div>
<div class="abs service-card" style="left:853px">
  <div class="service-photo" role="img" aria-label="Modern white accessory dwelling unit with lit entry" style="background:linear-gradient(180deg,#8fb0d8,#e8ecef 55%,#6a6e6a)"></div>
  <div class="service-name">Building ADU</div>
  <p class="service-copy">Ut enim ad minima veniamu is nostrum exercitationeull am corporis suscip.</p>
  <div class="service-more">READ MORE</div>
</div>

<!-- projects -->
<h2 class="abs section-title" style="top:1912px">Our Projects</h2>
<div class="abs project-tile" style="left:111px;top:2000px;background:linear-gradient(135deg,#e9e5df,#c7b9a6 60%,#8f7a62)" role="img" aria-label="Bright living room with brick walls and pendant lights"></div>
<div class="abs project-tile" style="left:441px;top:2000px;background:linear-gradient(180deg,#9fb2a2,#7a7468 50%,#a9a7a2)" role="img" aria-label="Stone house with paved driveway"></div>
<div class="abs project-tile" style="left:770px;top:2000px;background:linear-gradient(135deg,#efe9e1,#d9c7b0 55%,#9a6d44)" role="img" aria-label="Living room with cream sofa and wood floor"></div>
<div class="abs project-tile" style="left:111px;top:2246px;background:linear-gradient(180deg,#d7dde3,#aeb3b6 50%,#6b8f46)" role="img" aria-label="Grey two-storey house with front lawn"></div>
<div class="abs project-tile" style="left:441px;top:2246px;background:linear-gradient(135deg,#eceae6,#b99a75 55%,#6a4a2e)" role="img" aria-label="Kitchen with wooden island and bar stools"></div>
<div class="abs project-tile" style="left:770px;top:2246px;background:linear-gradient(135deg,#e6e1d6,#a9a79c 55%,#7a7770)" role="img" aria-label="Bathroom with grey vanity and bathtub"></div>
<div class="abs btn" style="left:511px;top:2526px;width:178px;height:58px;font-size:16px">EXPLORE MORE</div>

<!-- testimonials -->
<div class="abs testimonial-band"></div>
<h2 class="abs section-title" style="top:2712px">Testimonials</h2>
<div class="abs quote-circle"></div>
<div class="abs quote-mark">“</div>
<div class="abs client-photo" role="img" aria-label="Portrait of a smiling client"></div>
<p class="abs quote-text">“ Nam libero tempore, cum soluta nobis est eligendi optio cumque nihil impedit quo minus id quod maxime placeat facere possimus, omnis voluptas assumenda est, omnis dolor repellendus eveniet ut et voluptates.”</p>
<div class="abs quote-name">- JOHN DOE</div>
<div class="abs dot-arrow" style="left:837px"><svg width="10" height="12" viewBox="0 0 10 12"><path d="M7 1L2 6l5 5" stroke="#fff" stroke-width="2.2" fill="none"/></svg></div>
<div class="abs dot-arrow" style="left:875px"><svg width="10" height="12" viewBox="0 0 10 12"><path d="M3 1l5 5-5 5" stroke="#fff" stroke-width="2.2" fill="none"/></svg></div>

<!-- contact -->
<h2 class="abs section-title" style="top:3152px">Contact Us</h2>
<div class="abs sub-title" style="left:110px;top:3248px">Request a Quote</div>
<div class="abs field" style="left:111px;top:3309px;width:297px;height:46px">Name :</div>
<div class="abs field" style="left:417px;top:3309px;width:297px;height:46px">Phone no :</div>
<div class="abs field" style="left:111px;top:3370px;width:603px;height:46px">Email :</div>
<div class="abs field" style="left:111px;top:3432px;width:603px;height:83px">Message :</div>
<div class="abs btn" style="left:617px;top:3533px;width:97px;height:44px;font-size:15px">SUBMIT</div>

<div class="abs sub-title" style="left:779px;top:3248px">Contact Information</div>
<div class="abs info-icon" style="top:3305px"><svg width="14" height="18" viewBox="0 0 14 18"><path d="M7 1a6 6 0 0 0-6 6c0 4.5 6 10 6 10s6-5.5 6-10a6 6 0 0 0-6-6z" fill="#f26f21"/><circle cx="7" cy="7" r="2.2" fill="#fff"/></svg></div>
<div class="abs info-text" style="top:3303px">27 Marden Close Ashby<br>eveniet ut et vol</div>
<div class="abs info-icon" style="top:3375px"><svg width="16" height="12" viewBox="0 0 16 12"><rect width="16" height="12" rx="2" fill="#f26f21"/><path d="M1 2l7 5 7-5" stroke="#fff" stroke-width="1.5" fill="none"/></svg></div>
<div class="abs info-text" style="top:3380px">info@bramwellbuildersca.example</div>
<div class="abs info-icon" style="top:3440px"><svg width="16" height="16" viewBox="0 0 16 16"><circle cx="8" cy="8" r="7.5" fill="#f26f21"/><path d="M1 8h14M8 1c-3 3-3 11 0 14M8 1c3 3 3 11 0 14" stroke="#fff" stroke-width="1.1" fill="none"/></svg></div>
<div class="abs info-text" style="top:3445px">www.bramwellbuildersca.example</div>
<div class="abs sub-title" style="left:779px;top:3500px">Social Media</div>
<div class="abs social-small" style="left:775px" role="img" aria-label="Social profile link"></div>
<div class="abs social-small" style="left:822px" role="img" aria-label="Social profile link"></div>
<div class="abs social-small" style="left:868px" role="img" aria-label="Social profile link"></div>

<div class="abs footer-rule"></div>
<p class="abs copyright">Copyright © 2020, Bramwell Builders. All rights reserved.</p>
<svg class="abs" style="left:1062px;top:3670px" width="28" height="16" viewBox="0 0 28 16"><path d="M2 14L14 3l12 11" stroke="#b9b9bd" stroke-width="2.5" fill="none"/></svg>

</body>
</html>
```